Consulting firm business card, email signature, stationery
Halverton Advisory Group
Use standard fonts
Same font or standard is fine
Peter L. Dravik
President
842 S. Tolliver Street
Fairbrook, MO 63199
pete.dravik@halvertonag.example
halvertonag.example
The font can be standard for a professional consulting firm, or you can try with matching the logo.
The business card and email signature are most important. Stationery would be a nice bonus.
Ai version of logo file

```html
<!DOCTYPE html>
<html lang="en">
<head>
<meta charset="utf-8">
<title>Halverton Advisory Group – Business Card</title>
<link rel="stylesheet" href="https://fonts.googleapis.com/css2?family=Cinzel:wght@400;600&family=Lato:wght@400&display=swap">
<style>
  :root {
    --canvas: #ecebe7;
    --card-white: #ffffff;
    --brand-green: #3f6b2f;
    --brand-green-dark: #2f5524;
    --brand-green-light: #5e8a47;
    --accent-orange: #e8661e;
    --accent-amber: #f3a13a;
    --ink: #3c3c3c;
    --ink-soft: #6b6b6b;
    --on-green: #ffffff;
  }
  * { box-sizing: border-box; margin: 0; padding: 0; }
  html, body { width: 1200px; height: 758px; overflow: hidden; }
  body { background: var(--canvas); position: relative; font-family: "Lato", Arial, sans-serif; }

  .card {
    position: absolute;
    top: 225px;
    width: 540px;
    height: 309px;
    border-radius: 18px;
    overflow: hidden;
    box-shadow: 0 6px 18px rgba(0,0,0,0.18);
  }
  .card-front { left: 40px; background: var(--card-white); }
  .card-back {
    left: 620px;
    background: radial-gradient(ellipse at 45% 35%, var(--brand-green-light), var(--brand-green) 55%, var(--brand-green-dark));
  }

  .front-swoosh { position: absolute; inset: 0; }

  .brand {
    position: absolute; left: 34px; top: 34px;
    display: flex; align-items: center; gap: 14px;
  }
  .brand-dot {
    width: 46px; height: 46px; border-radius: 50%;
    background: var(--brand-green);
  }
  .brand-name {
    font-family: "Cinzel", Georgia, serif; font-weight: 600;
    color: var(--brand-green-dark);
    font-size: 24px; line-height: 1.05; letter-spacing: 0.5px;
  }
  .brand-name span { display: block; font-size: 17px; letter-spacing: 1.5px; }

  .address {
    position: absolute; left: 34px; top: 112px;
    font-size: 13px; color: var(--ink-soft); letter-spacing: 0.3px;
  }

  .person {
    position: absolute; left: 34px; top: 238px;
    font-family: "Cinzel", Georgia, serif; color: var(--on-green); text-align: right;
    width: 210px;
  }
  .person-name { font-size: 17px; letter-spacing: 0.8px; }
  .person-title { font-size: 12px; letter-spacing: 1.5px; margin-top: 4px; }

  .divider {
    position: absolute; left: 258px; top: 214px;
    width: 1px; height: 74px; background: rgba(255,255,255,0.7);
  }

  .contacts {
    position: absolute; left: 270px; top: 212px;
    list-style: none; color: var(--on-green); font-size: 11.5px;
  }
  .contacts li { display: flex; align-items: center; gap: 7px; height: 19px; white-space: nowrap; }
  .contacts svg { width: 11px; height: 11px; flex: none; }

  .back-brand {
    position: absolute; left: 0; right: 0; top: 100px;
    display: flex; align-items: center; justify-content: center; gap: 14px;
  }
  .back-brand .brand-dot { background: transparent; border: 3px solid var(--on-green); width: 40px; height: 40px; }
  .back-brand .brand-name { color: var(--on-green); font-size: 22px; }
  .back-url {
    position: absolute; left: 0; right: 0; top: 238px; text-align: center;
    font-family: "Cinzel", Georgia, serif; color: var(--on-green);
    font-size: 15px; letter-spacing: 2px;
  }
</style>
</head>
<body>
  <section class="card card-front" aria-label="Business card front">
    <svg class="front-swoosh" viewBox="0 0 540 309" preserveAspectRatio="none" aria-hidden="true">
      <path d="M0 188 Q250 128 540 150 L540 309 L0 309 Z" fill="var(--brand-green)"/>
      <path d="M0 178 Q250 118 540 140" fill="none" stroke="var(--accent-amber)" stroke-width="5"/>
      <path d="M0 186 Q250 126 540 148" fill="none" stroke="var(--accent-orange)" stroke-width="6"/>
    </svg>

    <div class="brand">
      <div class="brand-dot"></div>
      <div class="brand-name">Halverton<span>Advisory Group</span></div>
    </div>
    <p class="address">842 S. Tolliver Street, Fairbrook, MO 63199</p>

    <div class="person">
      <p class="person-name">Peter L. Dravik</p>
      <p class="person-title">President</p>
    </div>
    <div class="divider"></div>
    <ul class="contacts">
      <li><svg viewBox="0 0 12 12"><path d="M3 1 L5 4 L4 5 Q5 7 7 8 L8 7 L11 9 L10 11 Q4 11 1 2 Z" fill="currentColor"/></svg>314-555-0142</li>
      <li><svg viewBox="0 0 12 12"><rect x="3" y="1" width="6" height="10" rx="1" fill="none" stroke="currentColor" stroke-width="1.4"/></svg>314-555-0186</li>
      <li><svg viewBox="0 0 12 12"><rect x="1" y="2.5" width="10" height="7" fill="none" stroke="currentColor" stroke-width="1.2"/><path d="M1 2.5 L6 7 L11 2.5" fill="none" stroke="currentColor" stroke-width="1.2"/></svg>pete.dravik@halvertonag.example</li>
      <li><svg viewBox="0 0 12 12"><circle cx="6" cy="6" r="5" fill="none" stroke="currentColor" stroke-width="1.2"/><path d="M1 6 H11 M6 1 Q3 6 6 11 Q9 6 6 1" fill="none" stroke="currentColor" stroke-width="1"/></svg>www.halvertonag.example</li>
    </ul>
  </section>

  <section class="card card-back" aria-label="Business card back">
    <div class="back-brand">
      <div class="brand-dot"></div>
      <div class="brand-name">Halverton<span>Advisory Group</span></div>
    </div>
    <p class="back-url">WWW.HALVERTONAG.EXAMPLE</p>
  </section>
</body>
</html>
```